Halvern Ridge Hospital

We need a template for our hospital newsletter.

I am attaching what we did for December and also what we did for January. We like the January one better, but we need to keep the old style calendar.

I am also attaching the logo.

We need the document to be easily editable so that we can change the content month to month.

Industry/Entity Type

Hospital

```html
<!DOCTYPE html>
<html lang="en">
<head>
<meta charset="utf-8">
<title>Halvern Ridge Hospital – Specialty Clinic Calendar</title>
<link href="https://fonts.googleapis.com/css2?family=Open+Sans:wght@400;700&family=Roboto+Condensed:wght@400;700&family=Roboto:wght@700&display=swap" rel="stylesheet">
<style>
  :root{
    --ink:#111;
    --black:#000;
    --page:#fff;
    --red:#e0200f;
    --blue:#1a5ee0;
    --grid:#8c8c8c;
    --footer:#4e4b48;
    --icon:#3b7bbf;
  }
  *{box-sizing:border-box;margin:0;padding:0}
  html,body{width:827px;height:1200px;overflow:hidden;background:var(--black)}
  .canvas{position:relative;width:827px;height:1200px;background:var(--black);font-family:"Open Sans",Arial,sans-serif;color:var(--ink)}
  .page{position:absolute;left:29px;top:0;width:769px;height:1034px;background:var(--page)}

  .topbar{position:absolute;left:29px;top:0;width:664px;height:19px;background:var(--red);color:#fff;font-family:"Roboto",Arial,sans-serif;font-weight:700;font-size:14px;line-height:16px}
  .topbar .issue{position:absolute;left:22px;top:0}
  .topbar .site{position:absolute;left:240px;top:0;font-size:15px}
  .topbar .date{position:absolute;left:562px;top:0;font-size:11.5px;font-weight:400}
  .social{position:absolute;left:693px;top:0;width:105px;height:19px;background:#fff;border:1px solid var(--red);border-top:0;display:flex;gap:5px;justify-content:center;align-items:center}
  .social span{width:12px;height:12px;background:var(--icon);border-radius:2px}

  .month-bar{position:absolute;left:49px;top:43px;width:730px;height:34px;background:var(--blue);color:#fff;font-family:"Roboto",Arial,sans-serif;font-weight:700;font-size:16px;text-align:center;line-height:34px;letter-spacing:.3px}

  .calendar{position:absolute;left:50px;top:82px;width:728px;border-collapse:collapse;table-layout:fixed}
  .calendar th{font-family:"Roboto",Arial,sans-serif;font-weight:700;font-size:13px;height:17px;line-height:17px;border-bottom:2px solid var(--ink);padding:0}
  .calendar td{border:1px solid var(--grid);vertical-align:top;padding:6px 0 0 5px;font-size:9.8px;line-height:14.5px;overflow:hidden}
  .calendar tr.r1 td{height:104px}
  .calendar tr.r2 td{height:115px}
  .calendar tr.r3 td{height:106px}
  .calendar tr.r4 td{height:112px}
  .calendar tr.r5 td{height:107px}
  .cell{display:flex;white-space:nowrap}
  .day{width:21px;flex:none}
  .clinic{font-weight:700;letter-spacing:-.1px}
  .gap{height:14.5px}

  .footer{position:absolute;left:29px;top:1034px;width:769px;height:110px;background:var(--footer);color:#fff;font-family:"Roboto Condensed",Arial,sans-serif}
  .footer h3{position:absolute;left:9px;top:5px;font-weight:400;font-size:17px}
  .services{position:absolute;top:6px;list-style:none;font-size:13.5px;line-height:21px}
  .services li::before{content:"";display:inline-block;width:5px;height:5px;border-radius:50%;background:#fff;margin:0 9px 2px 0}
  .services.col-a{left:125px}
  .services.col-b{left:354px}
  .callout{position:absolute;left:570px;top:16px;width:182px;text-align:center;font-weight:700;font-size:13.5px;line-height:18px}
  .callout .phone{font-size:21px;line-height:30px;margin-top:3px}
  .copyright{position:absolute;left:29px;top:1144px;width:769px;height:30px;background:var(--blue);color:#fff;font-family:"Roboto Condensed",Arial,sans-serif;font-size:12px;text-align:center;line-height:30px}
</style>
</head>
<body>
<div class="canvas">
  <div class="page"></div>

  <header class="topbar">
    <span class="issue">ISSUE : 01</span>
    <span class="site">www.halvernridgehospital.org</span>
    <span class="date">29 JULY 2014</span>
  </header>
  <div class="social" aria-label="Social links"><span></span><span></span><span></span><span></span><span></span></div>

  <div class="month-bar">DECEMBER 2015</div>

  <table class="calendar">
    <colgroup><col style="width:147px"><col style="width:150px"><col style="width:147px"><col style="width:140px"><col style="width:144px"></colgroup>
    <thead><tr><th>MONDAY</th><th>TUESDAY</th><th>WEDNESDAY</th><th>THURSDAY</th><th>FRIDAY</th></tr></thead>
    <tbody>
      <tr class="r1">
        <td><div class="cell"><span class="day">1</span></div></td>
        <td><div class="cell"><span class="day">2</span><div><div class="clinic">Surgery/Vascular</div><div>Marcus Holloway, DO</div></div></div></td>
        <td><div class="cell"><span class="day">3</span><div><div class="clinic">Surgery/Vascular</div><div>Marcus Holloway, DO</div><div class="clinic">Podiatry</div><div>Glen Harrow, DPM</div><div class="clinic">Oncology / Hematology</div><div>Alan Corvell, MD</div></div></div></td>
        <td><div class="cell"><span class="day">4</span><div><div class="clinic">General Surgery</div><div>Peter Ansell, DO</div><div class="clinic">Stride Orthotics</div><div>Lewis Brandt</div><div>Call 555-201-4480</div></div></div></td>
        <td><div class="cell"><span class="day">5</span><div><div class="clinic">Surgery/Vascular</div><div>Marcus Holloway, DO</div></div></div></td>
      </tr>
      <tr class="r2">
        <td><div class="cell"><span class="day">8</span><div><div class="clinic">Pain Services</div><div>Owen Tate CRNA</div></div></div></td>
        <td><div class="cell"><span class="day">9</span><div><div class="clinic">Surgery/Vascular</div><div>Marcus Holloway, DO</div><div class="gap"></div><div class="clinic">Urology</div><div>Sean Morley, MD</div></div></div></td>
        <td><div class="cell"><span class="day">10</span><div><div class="clinic">General Surgery</div><div>Peter Ansell, DO</div><div class="gap"></div><div class="clinic">Oncology / Hematology</div><div>Alan Corvell, MD</div></div></div></td>
        <td><div class="cell"><span class="day">11</span><div><div class="clinic">Pulmonary Clinic</div><div>Neil Foster, DO</div><div class="clinic">General Surgery</div><div>Peter Ansell, DO</div><div class="clinic">Hearing Aid Specialist</div><div>Dale Whitcomb, H.I.S.</div></div></div></td>
        <td><div class="cell"><span class="day">12</span><div><div class="clinic">Surgery/Vascular</div><div>Marcus Holloway, DO</div><div class="gap"></div><div class="clinic">Podiatry</div><div>Glen Harrow, DPM</div></div></div></td>
      </tr>
      <tr class="r3">
        <td><div class="cell"><span class="day">13</span></div></td>
        <td><div class="cell"><span class="day">16</span><div><div class="clinic">Surgery/Vascular</div><div>Marcus Holloway, DO</div><div class="clinic">ENT</div><div>Carl Denning, MD</div><div class="clinic">Dermatology</div><div>Ruth Callow , PA-C</div></div></div></td>
        <td><div class="cell"><span class="day">17</span><div><div class="clinic">Surgery/Vascular</div><div>Marcus Holloway, DO</div><div class="clinic">Podiatry</div><div>Glen Harrow, DPM</div><div class="clinic">Oncology / Hematology</div><div>Alan Corvell, MD</div></div></div></td>
        <td><div class="cell"><span class="day">18</span><div><div class="clinic">Lake Orthopaedic</div><div>Martin Quill, MD</div><div class="gap"></div><div class="clinic">General Surgery</div><div>Peter Ansell, DO</div></div></div></td>
        <td><div class="cell"><span class="day">18</span><div><div class="clinic">Surgery/Vascular</div><div>Marcus Holloway, DO</div></div></div></td>
      </tr>
      <tr class="r4">
        <td><div class="cell"><span class="day">22</span><div><div class="clinic">Cardiology</div><div>Lake Heart Center</div><div>Evan Stroud, MD</div><div class="clinic">Lake Heart Device Clinic</div><div>Call 555-318-0927</div><div class="clinic">Podiatry</div><div>Glen Harrow, DPM</div></div></div></td>
        <td><div class="cell"><span class="day">23</span><div><div class="clinic">Surgery/Vascular</div><div>Marcus Holloway, DO</div></div></div></td>
        <td><div class="cell"><span class="day">24</span><div><div class="clinic">General Surgery</div><div>Peter Ansell, DO</div></div></div></td>
        <td><div class="cell"><span class="day">25</span></div></td>
        <td><div class="cell"><span class="day">26</span></div></td>
      </tr>
      <tr class="r5">
        <td><div class="cell"><span class="day">29</span><div><div class="clinic">Pain Services</div><div>Owen Tate CRNA</div></div></div></td>
        <td><div class="cell"><span class="day">30</span><div><div class="clinic">Surgery/Vascular</div><div>Marcus Holloway, DO</div></div></div></td>
        <td><div class="cell"><span class="day">31</span><div><div class="clinic">Podiatry</div><div>Glen Harrow, DPM</div><div class="clinic">General Surgery</div><div>Peter Ansell, DO</div><div class="clinic">Oncology / Hematology</div><div>Alan Corvell, MD</div></div></div></td>
        <td></td>
        <td><div class="cell"><span class="day">27</span></div></td>
      </tr>
    </tbody>
  </table>

  <footer class="footer">
    <h3>Other Services :</h3>
    <ul class="services col-a">
      <li>Nuclear Stress Test</li>
      <li>Ultrasound</li>
      <li>Lymphedema Therapy</li>
      <li>Skilled / Respite/Hospice</li>
      <li>Nuclear Medicine-Friday</li>
    </ul>
    <ul class="services col-b">
      <li>24 Hour Emergency Room</li>
      <li>Vascular Studies-Mon. &amp;Wed.</li>
      <li>DOT Drug &amp; Alcohol Screening</li>
      <li>Chemo/Infusion Therapy</li>
      <li>Respiratory Therapy</li>
    </ul>
    <div class="callout">
      <div>CALL US FOR</div>
      <div>IMERGENCY SERVICE</div>
      <div>Specialty Clinic</div>
      <div class="phone">(555) 730- 4162</div>
    </div>
  </footer>
  <div class="copyright">Copyright © 2015 Halvern Ridge Hospital &nbsp; All Rights Reserved.</div>
</div>
</body>
</html>
```